We are an education and business training and consulting company focused on helping companies maximize their growth potential. Our goal is provide targeted human resource solutions to organizational problems.
Target Market(s)
School districts and businesses of all types
Industry/Entity Type
Education
Contact Information for Business Card
Crestline and Harbor Partners LLC
Walter Pruitt president
Business and Education Training and Consulting
517 Birch Hollow Lane
Naples, Florida 34987
(239) 555-0147
Walter.pruitt@crestlineharborpartners.example
Font styles to use
Colors
Designer to choose colors to be used in the design.
Look and feel

```html
<!DOCTYPE html>
<html lang="en">
<head>
<meta charset="utf-8">
<title>Crestline and Harbor Partners LLC – Business Card</title>
<link rel="stylesheet" href="https://fonts.googleapis.com/css2?family=Arimo:wght@400&family=Tenor+Sans&family=Tinos:ital,wght@1,400;1,700&display=swap">
<style>
  :root {
    --page: #e6e8ec;
    --card: #ffffff;
    --band: #6289c9;
    --band-dark: #4f76b8;
    --brand: #4d7ac6;
    --maroon: #7a1550;
    --ink-blue: #1f4fa0;
    --white: #ffffff;
  }
  * { box-sizing: border-box; margin: 0; padding: 0; }
  html, body {
    width: 1200px; height: 1200px; overflow: hidden;
    background: var(--page);
  }
  .canvas {
    position: relative; width: 1200px; height: 1200px;
  }
  .card {
    position: absolute; left: 150px; width: 900px; height: 514px;
    background: var(--card);
    box-shadow: 0 10px 28px rgba(30, 40, 60, 0.18);
    overflow: hidden;
  }
  .card--front { top: 56px; }
  .card--back { top: 630px; }
  .card__bands { position: absolute; inset: 0; width: 900px; height: 514px; }
  .card__bands .band { fill: var(--band); }

  /* Front */
  .brand {
    position: absolute; left: 0; right: 0; top: 170px;
    text-align: center; color: var(--brand);
    font-family: "Arimo", Arial, sans-serif; font-weight: 400;
  }
  .brand__name { font-size: 56px; line-height: 1.1; letter-spacing: 0.5px; }
  .brand__sub {
    display: flex; align-items: center; justify-content: center; gap: 14px;
    font-size: 30px; margin-top: 8px;
  }
  .brand__rule { width: 50px; height: 2px; background: var(--brand); }

  /* Back */
  .back__title {
    position: absolute; left: 0; right: 0; top: 34px;
    text-align: center; color: var(--white);
    font-family: "Tenor Sans", "Trebuchet MS", sans-serif;
    font-size: 38px; letter-spacing: 0.5px;
  }
  .contact {
    position: absolute; left: 0; right: 0; top: 168px;
    text-align: center;
    font-family: "Tinos", "Times New Roman", serif;
    font-style: italic; font-weight: 700; font-size: 28px; line-height: 1.9;
  }
  .contact__address { color: var(--maroon); }
  .contact__phone, .contact__email { color: var(--ink-blue); }
  .back__footer {
    position: absolute; left: 34px; bottom: 18px;
    color: var(--white);
    font-family: "Tinos", "Times New Roman", serif;
    font-style: italic; font-size: 26px;
  }
</style>
</head>
<body>
<main class="canvas">

  <section class="card card--front" aria-label="Business card front">
    <svg class="card__bands" viewBox="0 0 900 514" aria-hidden="true">
      <polygon class="band" points="0,0 900,0 900,14 800,14 776,42 124,42 100,14 0,14"/>
      <polygon class="band" points="0,514 0,468 70,468 96,436 804,436 830,468 900,468 900,514"/>
    </svg>
    <div class="brand">
      <div class="brand__name">Crestline and Harbor</div>
      <div class="brand__sub">
        <span class="brand__rule"></span>
        <span>Partners LLC</span>
        <span class="brand__rule"></span>
      </div>
    </div>
  </section>

  <section class="card card--back" aria-label="Business card back">
    <svg class="card__bands" viewBox="0 0 900 514" aria-hidden="true">
      <rect class="band" x="0" y="0" width="900" height="16"/>
      <rect class="band" x="0" y="24" width="900" height="88"/>
      <polygon class="band" points="0,514 0,456 310,456 330,412 550,412 570,456 900,456 900,514"/>
      <polygon fill="#ffffff" points="440,422 450,440 430,440"/>
    </svg>
    <h1 class="back__title">Crestline and Harbor Partners LLC</h1>
    <div class="contact">
      <p class="contact__address">Address : 517 Birch Hollow Lane Naples, Florida 34987</p>
      <p class="contact__phone">Phone : (239) 555-0147</p>
      <p class="contact__email">Email : Walter.pruitt@crestlineharborpartners.example</p>
    </div>
    <p class="back__footer">Walter Pruitt president Business and Education Training and Consulting</p>
  </section>

</main>
</body>
</html>
```